Business card for different employees

A professional new updated design incorporating our current business's color themes and styles such as our on-site service trucks decals included in pictures attached. Our current business card is very simple and not professionally designed. We are a small family business but want a professional corporate look.

Target Market(s)

Cards to be handed out to new customers , corperate meetings. For our on site service operators.

Industry/Entity Type

Hydraulic

Contact Information for Business Card

Address, website, phone number, email, logo.
slogan - "Industry chosen hose and fittings provider".
24/7 on-site service , supply and hose management
Experienced , indpendant , family owned

Font styles to use
Sans Serif

Requirements
Must have
• Easily editable so that I can add different names and different roles for employees etc.
Nice to have
• Freedom with colour doesn't necessarily have to be blue but that is our company colour theme with trucks and logo so makes sense for the card to have blue like the trucks.

```html
<!DOCTYPE html>
<html lang="en">
<head>
<meta charset="utf-8">
<title>Meridian Hose &amp; Fittings – Business Card</title>
<link href="https://fonts.googleapis.com/css2?family=Roboto+Condensed:ital,wght@0,400;0,700;1,700&display=swap" rel="stylesheet">
<style>
  :root {
    --bg: #141414;
    --paper: #ffffff;
    --brand-blue: #2f3bb0;
    --brand-blue-deep: #23288a;
    --brand-blue-light: #4652c4;
    --ink: #111111;
    --ink-navy: #0e1040;
    --mark-dark: #1c1c1c;
    --white: #ffffff;
  }
  * { box-sizing: border-box; margin: 0; padding: 0; }
  html, body {
    width: 1200px; height: 900px; overflow: hidden;
    background: var(--bg);
    font-family: "Roboto Condensed", Arial, sans-serif;
  }
  .canvas {
    position: relative; width: 1200px; height: 900px;
    display: flex; align-items: center; justify-content: center; gap: 40px;
  }
  .card {
    position: relative; width: 540px; height: 320px;
    background: var(--paper); border-radius: 22px; overflow: hidden;
  }

  /* ---------- Contact side ---------- */
  .brand-lockup {
    position: absolute; left: 26px; top: 24px;
    display: flex; align-items: center; gap: 8px;
  }
  .brand-dot { width: 22px; height: 22px; border-radius: 50%; background: var(--mark-dark); }
  .brand-name {
    font-weight: 700; font-size: 15px; letter-spacing: .5px;
    color: var(--brand-blue); text-transform: uppercase;
  }
  .person { position: absolute; left: 26px; top: 58px; }
  .person-name { font-weight: 700; font-size: 28px; color: var(--ink); line-height: 1; }
  .person-title { font-weight: 700; font-size: 13px; color: var(--brand-blue); margin-top: 4px; letter-spacing: .5px; }

  .contact-band {
    position: absolute; left: 0; height: 30px;
    background: var(--brand-blue);
    clip-path: polygon(0 0, 100% 0, calc(100% - 18px) 100%, 0 100%);
    display: flex; align-items: center; gap: 10px; padding-left: 22px;
    color: var(--white); font-size: 15px;
  }
  .contact-band svg { width: 14px; height: 14px; fill: var(--white); flex: none; }
  .band-address { top: 118px; width: 280px; }
  .band-email { top: 156px; width: 258px; }
  .band-phone { top: 194px; width: 236px; }

  .service-panel {
    position: absolute; inset: 0;
    background: linear-gradient(135deg, var(--brand-blue-light), var(--brand-blue-deep));
    clip-path: polygon(300px 170px, 540px 170px, 540px 320px, 150px 320px, 150px 250px, 250px 238px);
  }
  .service-list {
    position: absolute; left: 316px; top: 180px; width: 210px;
    list-style: none; color: var(--white); font-size: 13px; line-height: 1.25;
  }
  .service-list li { position: relative; padding-left: 12px; margin-bottom: 5px; }
  .service-list li::before {
    content: ""; position: absolute; left: 0; top: 6px;
    width: 5px; height: 5px; border-radius: 50%; background: var(--white);
  }
  .service-tagline {
    position: absolute; left: 268px; top: 252px;
    color: var(--white); font-size: 21px; font-weight: 400;
  }
  .service-web {
    position: absolute; left: 176px; top: 286px;
    color: var(--ink-navy); font-size: 18px; font-weight: 700; letter-spacing: .5px;
  }

  /* ---------- Brand side ---------- */
  .brand-mark {
    position: absolute; left: 40px; top: 40px;
    width: 170px; height: 170px; border-radius: 50%; background: var(--mark-dark);
  }
  .brand-title {
    position: absolute; left: 190px; top: 196px; width: 320px;
    padding: 8px 14px; background: transparent;
    font-weight: 700; font-size: 26px; line-height: 1.05; letter-spacing: 1px;
    color: var(--brand-blue); text-transform: uppercase;
  }
  .brand-values {
    position: absolute; left: 204px; top: 268px;
    font-weight: 700; font-style: italic; font-size: 12px; letter-spacing: .6px;
    color: var(--brand-blue);
  }
  .edge-tab {
    position: absolute; right: 0; top: 238px; width: 8px; height: 26px;
    background: var(--brand-blue);
  }
</style>
</head>
<body>
<main class="canvas">

  <section class="card card-contact" aria-label="Business card, contact side">
    <div class="brand-lockup">
      <span class="brand-dot"></span>
      <span class="brand-name">Meridian Hose &amp; Fittings</span>
    </div>
    <div class="person">
      <p class="person-name">YOUR NAME</p>
      <p class="person-title">JOB TITLE</p>
    </div>

    <div class="contact-band band-address">
      <svg viewBox="0 0 24 24"><path d="M12 2a7 7 0 0 0-7 7c0 5 7 13 7 13s7-8 7-13a7 7 0 0 0-7-7zm0 9.5A2.5 2.5 0 1 1 12 6.5a2.5 2.5 0 0 1 0 5z"/></svg>
      <span>Your Address Here</span>
    </div>
    <div class="contact-band band-email">
      <svg viewBox="0 0 24 24"><path d="M2 5h20v14H2zm2 2v.5l8 5 8-5V7l-8 5z"/></svg>
      <span>Youremail@xyz.com</span>
    </div>
    <div class="contact-band band-phone">
      <svg viewBox="0 0 24 24"><path d="M6.6 10.8a15 15 0 0 0 6.6 6.6l2.2-2.2a1 1 0 0 1 1-.25 11.4 11.4 0 0 0 3.6.57 1 1 0 0 1 1 1V20a1 1 0 0 1-1 1A17 17 0 0 1 3 4a1 1 0 0 1 1-1h3.5a1 1 0 0 1 1 1c0 1.25.2 2.45.57 3.57a1 1 0 0 1-.25 1z"/></svg>
      <span>00 0000 0000</span>
    </div>

    <div class="service-panel"></div>
    <ul class="service-list">
      <li>Hydraulic and Industrial Hose for all applications</li>
      <li>Sales, Supply and Hose Management</li>
    </ul>
    <p class="service-tagline">Fast Reliable Service 24/7</p>
    <p class="service-web">WWW.MERIDIANHOSE.COM.AU</p>
  </section>

  <section class="card card-brand" aria-label="Business card, brand side">
    <div class="brand-mark"></div>
    <p class="brand-title">Meridian Hose &amp; Fittings</p>
    <p class="brand-values">EXPERIENCED. &nbsp;INDPENDANT. &nbsp;FAMILY OWNED</p>
    <span class="edge-tab"></span>
  </section>

</main>
</body>
</html>
```